Web Design Project

We are re-starting this project.

This project is for a totally new look and design of a website for Wablor. www.wablor-demo.net.

Wablor is a naming protocol for physical locations and can be used for fixed and mobile people, places and things. Find your friends, or find a business. Because Wablor locations point to precise geo-physical (GPS) co-ordinates, navigation to a location becomes totally reliable.
Updates

Please see the modified brief for this project

Target Market(s)

Every person and every business can have multiple !Wabs (Wablor locations), so the website needs to be appealing and fun, but easy to use and functional

Industry/Entity Type

Business

Colors
34a6d7

Requirements
Must have
• Uniqueness!

```html
<!DOCTYPE html>
<html lang="en">
<head>
<meta charset="utf-8">
<title>Wablor – Find any place</title>
<link href="https://fonts.googleapis.com/css2?family=Questrial&family=Montserrat:wght@400;600;700&display=swap" rel="stylesheet">
<style>
  :root{
    --brand:#34a6d7;
    --brand-dark:#1e95d0;
    --yellow:#fbc21a;
    --grey-btn:#6e7d7a;
    --footer:#1e1f24;
    --footer-deep:#16171b;
    --text-light:#e8e8e8;
    --text-muted:#c9c9c9;
    --rule:#3a3b41;
    --chat:#b3c31b;
    --nav:#555;
  }
  *{margin:0;padding:0;box-sizing:border-box}
  html,body{width:1200px;height:1093px;overflow:hidden;background:#fff}
  body{position:relative;font-family:"Questrial",sans-serif}
  .abs{position:absolute}

  .site-header{position:absolute;left:0;top:0;width:1200px;height:49px;background:#fff}
  .brand{left:197px;top:6px;display:flex;align-items:center;gap:6px;font-family:"Montserrat",sans-serif;font-weight:700;font-size:27px;color:var(--brand)}
  .brand-dot{width:12px;height:12px;border-radius:50%;background:var(--brand)}
  .nav a{position:absolute;top:18px;font-family:"Montserrat",sans-serif;font-size:11px;color:var(--nav);text-decoration:none;letter-spacing:.2px}
  .nav a.active{color:var(--brand)}
  .btn-head{top:9px;height:30px;display:flex;align-items:center;justify-content:center;font-family:"Montserrat",sans-serif;font-weight:600;font-size:12px;color:#fff}
  .btn-signup{left:811px;width:91px;background:var(--yellow)}
  .btn-login{left:911px;width:92px;background:var(--grey-btn)}

  .hero{left:0;top:49px;width:1200px;height:650px;
    background:linear-gradient(180deg,#8a9fb3 0%,#9fa9ad 20%,#b7a58a 38%,#a77f55 60%,#8f6a45 80%,#7a5d42 100%)}
  .hero-title{left:197px;top:111px;font-family:"Montserrat",sans-serif;font-weight:700;font-size:24px;line-height:28px;color:#fff;text-transform:uppercase}
  .hero-title em{font-style:normal;color:var(--yellow)}
  .search-panel{left:197px;top:228px;width:374px;height:177px;background:rgba(30,30,35,.55)}
  .field{position:absolute;background:#fff;font-style:italic;font-size:11px;color:#888;display:flex;align-items:center}
  .field-keyword{left:17px;top:18px;width:339px;height:36px;justify-content:center}
  .field-select{top:71px;height:36px;padding-left:15px}
  .field-cat{left:17px;width:125px}
  .field-loc{left:191px;width:126px}
  .field-select::after{content:"";position:absolute;right:0;top:0;width:17px;height:36px;border-left:1px solid #ddd;
    background:linear-gradient(#777,#777) no-repeat}
  .caret{position:absolute;right:4px;top:15px;width:0;height:0;border-left:4px solid transparent;border-right:4px solid transparent;border-top:6px solid #777}
  .icon-btn{position:absolute;top:71px;width:39px;height:36px;background:var(--yellow);display:flex;align-items:center;justify-content:center}
  .search-btn{left:17px;top:126px;width:340px;height:35px;background:var(--brand-dark);color:#fff;font-family:"Montserrat",sans-serif;font-weight:600;font-size:11px;display:flex;align-items:center;justify-content:center}

  .social{top:684px;left:512px;display:flex;gap:16px}
  .social span{width:32px;height:32px;border-radius:50%;border:3px solid #fff}
  .s1{background:#3b5998}.s2{background:#1da1e2}.s3{background:#1e7bb5}.s4{background:#dd4b39}

  .site-footer{left:0;top:699px;width:1200px;height:350px;background:var(--footer)}
  .newsletter-title{left:0;width:1200px;top:43px;text-align:center;font-family:"Montserrat",sans-serif;font-weight:600;font-size:11px;color:#fff}
  .newsletter-input{left:420px;top:86px;width:278px;height:33px;background:#fff;font-style:italic;font-size:10px;color:#999;padding-left:10px;display:flex;align-items:center}
  .newsletter-btn{left:698px;top:86px;width:83px;height:33px;background:var(--brand-dark);color:#fff;font-family:"Montserrat",sans-serif;font-weight:600;font-size:10px;display:flex;align-items:center;justify-content:center}
  .col{top:157px;width:190px}
  .col h3{font-weight:400;font-size:14px;color:var(--text-light);padding-bottom:9px;border-bottom:1px solid var(--rule);margin-bottom:11px}
  .col p{font-size:11px;line-height:18px;color:var(--text-muted)}
  .col ul{list-style:none}
  .col li{font-family:"Montserrat",sans-serif;font-weight:600;font-size:10.5px;line-height:19px;color:var(--brand-dark)}

  .bottom-bar{left:0;top:1049px;width:1200px;height:44px;background:var(--footer-deep)}
  .copyright{left:0;width:1200px;top:15px;text-align:center;font-family:"Montserrat",sans-serif;font-weight:600;font-size:9.5px;color:#fff}
  .copyright span{color:var(--brand)}
  .chat{left:987px;top:7px;width:119px;height:37px;background:var(--chat);display:flex;align-items:center;justify-content:center;gap:8px;font-size:11px;color:#222}
</style>
</head>
<body>
  <header class="site-header">
    <div class="abs brand"><span>Wablor</span><span class="brand-dot"></span></div>
    <nav class="nav">
      <a class="active" style="left:392px">HOME</a>
      <a style="left:471px">ABOUT</a>
      <a style="left:557px">GATEGORIES</a>
      <a style="left:669px">CONTACT</a>
    </nav>
    <div class="abs btn-head btn-signup">SIGN UP</div>
    <div class="abs btn-head btn-login">LOGIN</div>
  </header>

  <section class="abs hero" role="img" aria-label="Aerial photograph of a European city with a river, bridges and autumn trees"></section>
  <h1 class="abs hero-title">Where ,would you<br><em>love</em> to go?<br>See, it’s easy?</h1>

  <div class="abs search-panel">
    <div class="field field-keyword">Search by keyword</div>
    <div class="field field-select field-cat">Categories<i class="caret"></i></div>
    <div class="icon-btn" style="left:145px">
      <svg width="14" height="16" viewBox="0 0 14 16"><g fill="#fff"><rect x="1" y="1" width="5" height="4"/><rect x="8" y="6" width="5" height="3"/><rect x="8" y="11" width="5" height="3"/><rect x="3" y="5" width="1.5" height="8"/><rect x="3" y="7" width="5" height="1.2"/><rect x="3" y="12" width="5" height="1.2"/></g></svg>
    </div>
    <div class="field field-select field-loc">Location<i class="caret"></i></div>
    <div class="icon-btn" style="left:318px">
      <svg width="12" height="16" viewBox="0 0 12 16"><path d="M6 0a6 6 0 0 0-6 6c0 4.5 6 10 6 10s6-5.5 6-10a6 6 0 0 0-6-6z" fill="#fff"/><circle cx="6" cy="6" r="2.2" fill="#fbc21a"/></svg>
    </div>
    <div class="abs search-btn">SEARCH ON MAP</div>
  </div>

  <footer class="abs site-footer">
    <div class="abs newsletter-title">SUBSCRIBE TO THE BEST OF OUR NEWSLETTER</div>
    <div class="abs newsletter-input">Type your email here !</div>
    <div class="abs newsletter-btn">SUBSCRIBE</div>

    <div class="abs col" style="left:197px">
      <h3>ABOUT US</h3>
      <p>Wablor is an Australian innovation company.Founded in 2012, Wablor has a vision to create the primary geo-physical address protocol in the digital world.</p>
    </div>
    <div class="abs col" style="left:402px">
      <h3>INFORMATION</h3>
      <ul><li>Privacy Policy</li><li>Terms and condition</li><li>Refuns</li><li>Help</li><li>FAQ</li></ul>
    </div>
    <div class="abs col" style="left:608px">
      <h3>LOCATION</h3>
      <ul><li>USA</li><li>Lebanen</li><li>Australie</li><li>France</li><li>Morocco</li></ul>
    </div>
    <div class="abs col" style="left:814px">
      <h3>CATEGORIES</h3>
      <ul><li>Hotels &amp; travel</li><li>Restaurant</li><li>Business</li><li>Friends</li><li>Public Places</li></ul>
    </div>
  </footer>

  <div class="abs social" aria-label="Social links">
    <span class="s1"></span><span class="s2"></span><span class="s3"></span><span class="s4"></span>
  </div>

  <div class="abs bottom-bar">
    <div class="abs copyright">Copyright 2014 © <span>Wablor-demo.net</span> - All right reserved</div>
    <div class="abs chat">
      <svg width="15" height="13" viewBox="0 0 15 13"><path d="M7.5 0C3.4 0 0 2.4 0 5.5c0 1.6.9 3 2.4 4L1.5 13l3.6-2.2c.8.2 1.6.3 2.4.3 4.1 0 7.5-2.5 7.5-5.6S11.6 0 7.5 0z" fill="#222"/></svg>
      Online chat
    </div>
  </div>
</body>
</html>
```